Industrial Professional Business Card Design (Vantrel Systems)

Would like professional looking business cards. Not too busy leaning towards minimal. Should have a slogan like:
"Industrial Automation and Control".

We are a tech company that programs industrial PLC computers. We also develop custom hardware solutions. Please use the logo for inspiration.

Target Market(s)

Mining, industrial, processing, automation, factory

Industry/Entity Type

Engineering

Contact Information for Business Card

Name, phone, email, website. job title.

Font styles to use
Other font styles liked:
• droid sans

Requirements
Must have
• Use colours that go well with the logo. Not too busy design.

```html
<!DOCTYPE html>
<html lang="en">
<head>
<meta charset="utf-8">
<title>Vantrel Systems – Business Card</title>
<link href="https://fonts.googleapis.com/css2?family=Noto+Sans:wght@400;600;700&display=swap" rel="stylesheet">
<style>
  :root {
    --navy: #1b2a5c;
    --band-blue: #1d4378;
    --orange: #f26d21;
    --white: #ffffff;
    --ink-blue: #1f4a7e;
    --text-grey: #3c4150;
    --stage: #e9e7e4;
  }
  * { box-sizing: border-box; margin: 0; padding: 0; }
  html, body { width: 1200px; height: 795px; overflow: hidden; }
  body {
    background: var(--stage);
    font-family: "Noto Sans", Arial, sans-serif;
    position: relative;
  }
  .card {
    position: absolute;
    width: 540px;
    height: 309px;
    top: 243px;
    box-shadow: 0 6px 18px rgba(0,0,0,.18);
    overflow: hidden;
  }
  /* Front */
  .card-front { left: 30px; background: var(--navy); }
  .front-mark {
    position: absolute; left: 0; right: 0; top: 0; bottom: 0;
    display: flex; align-items: center; justify-content: center; gap: 14px;
  }
  .mark-dot {
    width: 34px; height: 34px; border-radius: 50%;
    background: var(--orange); flex: none;
  }
  .front-name {
    color: var(--white); font-size: 38px; font-weight: 400; letter-spacing: -0.5px;
  }
  /* Back */
  .card-back { left: 630px; background: var(--white); }
  .back-mark {
    position: absolute; left: 28px; top: 92px;
    display: flex; align-items: center; gap: 10px;
  }
  .back-mark .mark-dot { width: 24px; height: 24px; }
  .back-name { color: var(--ink-blue); font-size: 25px; font-weight: 400; letter-spacing: -0.3px; }
  .divider {
    position: absolute; left: 282px; top: 52px; width: 2px; height: 128px;
    background: var(--orange);
  }
  .contact { position: absolute; left: 304px; top: 56px; }
  .person-name { color: var(--ink-blue); font-size: 22px; font-weight: 700; line-height: 1.05; }
  .person-title { color: var(--text-grey); font-size: 13px; margin-bottom: 18px; }
  .contact-line {
    display: flex; align-items: center; gap: 7px;
    color: var(--text-grey); font-size: 13.5px; line-height: 20px;
  }
  .contact-line svg { width: 11px; height: 11px; flex: none; }
  .rule-top {
    position: absolute; left: 0; right: 0; top: 194px; height: 2px; background: var(--orange);
  }
  .band {
    position: absolute; left: 0; right: 0; top: 199px; height: 62px;
    background: var(--band-blue); display: flex; align-items: center; padding-left: 28px;
  }
  .slogan { color: var(--white); font-size: 16px; letter-spacing: .2px; }
  .rule-bottom {
    position: absolute; left: 0; right: 0; top: 268px; height: 2px; background: var(--orange);
  }
</style>
</head>
<body>
  <section class="card card-front" aria-label="Business card front">
    <div class="front-mark">
      <span class="mark-dot"></span>
      <span class="front-name">Vantrel Systems</span>
    </div>
  </section>

  <section class="card card-back" aria-label="Business card back">
    <div class="back-mark">
      <span class="mark-dot"></span>
      <span class="back-name">Vantrel Systems</span>
    </div>
    <div class="divider"></div>
    <div class="contact">
      <p class="person-name">Dorian Kell</p>
      <p class="person-title">President</p>
      <p class="contact-line">
        <svg viewBox="0 0 12 12" aria-hidden="true"><path d="M2.5 1 L4.5 1 L5.2 3.6 L4 4.6 Q5 7 7.4 8 L8.4 6.8 L11 7.5 L11 9.5 Q10.5 11 9 11 Q1 10 1 3 Q1 1.5 2.5 1Z" fill="var(--orange)"/></svg>
        555-014-2290
      </p>
      <p class="contact-line">
        <svg viewBox="0 0 12 12" aria-hidden="true"><rect x="0.5" y="2.5" width="11" height="7" fill="var(--orange)"/><path d="M0.5 2.5 L6 6.5 L11.5 2.5" stroke="#fff" stroke-width="1" fill="none"/></svg>
        info@vantrelmailbox.com
      </p>
      <p class="contact-line">
        <svg viewBox="0 0 12 12" aria-hidden="true"><circle cx="6" cy="6" r="5.5" fill="var(--orange)"/><path d="M0.5 6 H11.5 M6 0.5 Q3 6 6 11.5 M6 0.5 Q9 6 6 11.5" stroke="#fff" stroke-width=".8" fill="none"/></svg>
        www.vantrelsite.com
      </p>
    </div>
    <div class="rule-top"></div>
    <div class="band"><p class="slogan">Industrial Automation and Control</p></div>
    <div class="rule-bottom"></div>
  </section>
</body>
</html>
```